Retractable Banner Design for Gentle Paws Carolina Rebrand

We need a retractable banner design for our market booth. I absolutely love our old banner design and would like to keep it clean and similar but more on theme with the new brand with the new colors. Full brand guide attached. Our slogan we would like to include is "professional pet care for when you can't be there" (dog walking & pet sitting).
Our services we would like to include is: Extended Visits, Pop In Visits, Dog Walking, Pet Taxi, Travel & Adventure Hikes.
We offer: Discounts for First Responders, Teachers, & Military
I would like to use elements from the brand as well as the colors. Include the website www.gentlepawsco.net somewhere

```html
<!DOCTYPE html>
<html lang="en">
<head>
<meta charset="utf-8">
<title>Gentle Paws Carolina – Retractable Banner</title>
<link href="https://fonts.googleapis.com/css2?family=Fraunces:opsz,wght@9..144,700;9..144,800&family=Poppins:wght@500;600;700&display=swap" rel="stylesheet">
<style>
  :root {
    --pink: #dc44a5;
    --teal: #1f6a80;
    --navy: #1c4e5e;
    --gold: #ecce6e;
    --cream: #fbf1dc;
    --white: #ffffff;
    --stage: #9c9c9c;
  }
  * { box-sizing: border-box; margin: 0; padding: 0; }
  html, body { width: 1200px; height: 1000px; overflow: hidden; }
  body { background: var(--stage); font-family: "Poppins", sans-serif; }
  .banner {
    position: absolute; left: 405px; top: 20px;
    width: 390px; height: 960px; background: var(--white); overflow: hidden;
  }
  .banner-bg { position: absolute; inset: 0; }
  .brand-name {
    position: absolute; top: 52px; left: 0; width: 100%; text-align: center;
    font-family: "Fraunces", serif; font-weight: 800; font-size: 36px; line-height: 1.05;
    color: var(--navy);
  }
  .headline { position: absolute; top: 240px; width: 100%; text-align: center; }
  .headline-main {
    font-family: "Fraunces", serif; font-weight: 800; font-size: 37px;
    color: var(--cream); letter-spacing: .5px;
  }
  .headline-pill {
    display: inline-block; margin-top: 4px; padding: 2px 26px;
    background: var(--gold); border-radius: 22px;
    font-family: "Fraunces", serif; font-weight: 800; font-size: 30px; color: var(--teal);
  }
  .tagline {
    margin-top: 10px; font-weight: 600; font-size: 16.5px; color: var(--cream); letter-spacing: .3px;
  }
  .photo {
    position: absolute; width: 100px; height: 100px; border-radius: 50%;
    border: 5px solid var(--white); box-shadow: 0 3px 8px rgba(0,0,0,.25);
  }
  .photo-1 { left: 20px; top: 387px; background: radial-gradient(circle at 50% 40%, #8aa36a, #4e5a3a); }
  .photo-2 { left: 140px; top: 387px; background: radial-gradient(circle at 50% 40%, #93a862, #48553a); }
  .photo-3 { left: 257px; top: 423px; background: linear-gradient(#a9c2dd, #7c8a8d 60%, #5e6364); }
  .services {
    position: absolute; left: 37px; top: 560px; width: 314px; height: 187px;
    border: 3px solid var(--gold); border-radius: 18px;
  }
  .services-title {
    position: absolute; left: 55px; top: -19px; width: 196px; height: 34px;
    background: var(--pink); color: var(--white); border-radius: 17px;
    text-align: center; line-height: 34px; font-weight: 600; font-size: 18px;
  }
  .service { position: absolute; width: 100px; text-align: center; color: var(--teal);
    font-weight: 500; font-size: 10.5px; line-height: 1.25; }
  .service svg { display: block; margin: 0 auto 4px; }
  .s1 { left: 12px; top: 25px; } .s2 { left: 107px; top: 25px; } .s3 { left: 200px; top: 25px; }
  .s4 { left: 58px; top: 102px; } .s5 { left: 155px; top: 102px; }
  .pets-strip {
    position: absolute; left: 0; top: 748px; width: 100%; height: 140px;
    background: linear-gradient(90deg, #e9e4df, #c59a6a 25%, #d99a55 40%, #6b4b35 55%, #8a5a3a 72%, #efeae6 92%);
  }
  .footer { position: absolute; left: 0; bottom: 0; width: 100%; height: 90px; background: var(--teal); }
  .offer {
    position: absolute; left: 72px; top: 838px; width: 248px; height: 68px;
    background: var(--cream); border: 3px solid var(--teal); border-radius: 34px;
    text-align: center; padding-top: 6px;
  }
  .offer-title { font-family: "Fraunces", serif; font-weight: 800; font-size: 20px; color: var(--pink); line-height: 1; }
  .offer-text { font-weight: 600; font-size: 10.5px; color: var(--navy); line-height: 1.3; margin-top: 2px; }
  .website {
    position: absolute; left: 0; bottom: 12px; width: 100%; text-align: center;
    font-weight: 700; font-size: 20px; color: var(--white);
  }
</style>
</head>
<body>
<main class="banner">
  <svg class="banner-bg" width="390" height="960" viewBox="0 0 390 960">
    <path d="M0 85 C90 215 300 215 390 80 L390 545 C300 470 120 560 0 480 Z" fill="var(--pink)"/>
    <path d="M0 120 C100 230 300 240 390 130 L390 145 C300 250 100 250 0 135 Z" fill="var(--white)"/>
    <path d="M0 135 C100 250 300 255 390 145 L390 160 C300 270 100 260 0 150 Z" fill="var(--gold)"/>
    <path d="M0 468 C120 540 280 410 390 500 L390 515 C280 430 120 560 0 485 Z" fill="var(--gold)"/>
  </svg>

  <div class="brand-name">Gentle Paws<br>Carolina</div>

  <section class="headline">
    <div class="headline-main">PROFESSIONAL</div>
    <div class="headline-pill">PET CARE</div>
    <div class="tagline">FOR WHEN YOU CAN'T BE THERE</div>
  </section>

  <div class="photo photo-1" role="img" aria-label="Pet sitter crouching outdoors with a brown dog"></div>
  <div class="photo photo-2" role="img" aria-label="Two pet sitters in a park with a dog"></div>
  <div class="photo photo-3" role="img" aria-label="Team members with a small dog beside a plane"></div>

  <section class="services">
    <div class="services-title">OUR SERVICES</div>
    <div class="service s1">
      <svg width="46" height="44" viewBox="0 0 46 44"><circle cx="20" cy="24" r="17" fill="none" stroke="var(--teal)" stroke-width="4"/><path d="M20 14v10l-6 6" stroke="var(--pink)" stroke-width="3" fill="none"/><circle cx="37" cy="8" r="7" fill="var(--pink)"/><path d="M37 4v8M33 8h8" stroke="#fff" stroke-width="2"/></svg>
      EXTENDED VISITS</div>
    <div class="service s2">
      <svg width="46" height="44" viewBox="0 0 46 44"><rect x="20" y="4" width="18" height="36" fill="var(--teal)"/><rect x="12" y="16" width="10" height="24" fill="var(--teal)"/><g fill="#fff"><rect x="24" y="9" width="4" height="4"/><rect x="31" y="9" width="4" height="4"/><rect x="24" y="17" width="4" height="4"/><rect x="31" y="17" width="4" height="4"/><rect x="24" y="25" width="4" height="4"/><rect x="31" y="25" width="4" height="4"/></g><path d="M9 24a7 7 0 0 1 7 7c0 5-7 11-7 11s-7-6-7-11a7 7 0 0 1 7-7z" fill="var(--pink)"/><circle cx="9" cy="31" r="2.5" fill="#fff"/></svg>
      POP IN VISITS</div>
    <div class="service s3">
      <svg width="50" height="46" viewBox="0 0 50 46"><circle cx="15" cy="5" r="4.5" fill="var(--teal)"/><path d="M15 11l-4 14 4 5-3 14M15 11l3 15 3 14M15 14l9 8" stroke="var(--teal)" stroke-width="4" fill="none" stroke-linecap="round"/><path d="M24 22l14 16" stroke="var(--pink)" stroke-width="1.5"/><path d="M34 36h10l2-4 2 1-2 5v4M36 38v4" stroke="var(--pink)" stroke-width="3" fill="none"/></svg>
      DOG WALKING</div>
    <div class="service s4">
      <svg width="62" height="40" viewBox="0 0 62 40"><path d="M4 20h10l8-9h18l8 9h10v10H4z" fill="var(--teal)"/><circle cx="16" cy="31" r="5" fill="var(--teal)" stroke="#fff" stroke-width="2"/><circle cx="46" cy="31" r="5" fill="var(--teal)" stroke="#fff" stroke-width="2"/><circle cx="10" cy="8" r="7" fill="var(--pink)"/><circle cx="10" cy="10" r="2" fill="#fff"/></svg>
      PET TAXI</div>
    <div class="service s5">
      <svg width="48" height="40" viewBox="0 0 48 40"><circle cx="24" cy="18" r="15" fill="var(--teal)"/><path d="M4 30l18-8 16-2-14 8z" fill="var(--teal)" stroke="#fff" stroke-width="1.5"/><path d="M36 14l8 10-6 12-6-12z" fill="var(--pink)"/></svg>
      TRAVEL &amp;<br>ADVENTURE HIKES</div>
  </section>

  <div class="pets-strip" role="img" aria-label="Row of pets: rabbits, dogs and a cat lined up side by side"></div>
  <div class="footer"></div>

  <div class="offer">
    <div class="offer-title">WE OFFER</div>
    <div class="offer-text">Discounts for First Responders,<br>Teachers, &amp; Military</div>
  </div>
  <div class="website">www.gentlepawsco.net</div>
</main>
</body>
</html>
```